Design a Brochure

Company Profile

About US

Povra is an on-demand delivery platform where you can order from restaurants, pharmacies, liquor and grocery stores.
This is the first online digital mall in Africa which will enable you to get back to what you care about which is serving the best liquor in the country.
Everything is delivered in less than one hour.
Customers uses a mobile app to connect with the stores that are within a 6 kilometers radius.
The nearest driver is notified instantly when there is an order that they need to attend to.
We empower communities to shop local with no waiting, and empower businesses through our API to offer delivery.
We make a real impact on your business when your product is featured in the app, new customers can discover it and loyal customers can have it more often.
Povra will provide all the relevant stakeholders with insight analytics, ratings and comments regarding all orders fulfilled online via Povra.

HOW IT WORKS?

Customers download the Povra app which is available for Orbit OS and Nimbus OS.
Customers register on the app.
Set the delivery location to see all the stores around.
Place the order for the item that you want.
Pay the cost of the items plus the delivery fee of R40.
Payments can be via Credit Card, Debit Cards or Cash on Delivery.
Track the progress of the order via the app.
Customers can also chat live with the driver or the Povra customer service team.
Once Povra has delivered, you are able to rate the service and also provide comments.

Introducing The team

>>>>>>>> Themba Curtis Mabasa (CEO )

He is experienced visioning, costing, innovation and executing projects from inception to launch and is able to provide a structured framework to analyze complex situations into simple strategic imperatives.

Started Povra as an e-Commerce platform then change the platform to become an on-demand delivery platform which now employers 10 full-time members and 20 independent contractors.

>>>>>>>> Richard Molapisi (CTO )

16 years of broad experience in enterprise software architecture, design and [url removed, login to view] in all stages of software development lifecycle. Experience in scalable and highly available systems. Exceptional understanding of the web infrastructure and ecosystem. Experienced team lead; works well with team members and customers.

Former Head of Architecture at KELTA leading the Architecture Team and also the Lead Architecture of
KELTA Webline Account Portal Project.

>>>>>>>> Lesedi Maphanga (Developer )

Accomplished Software Engineer specializing in object-oriented approaches to mobile development. Extensive background in full life-cycle of software development process including requirements gathering, design, coding, testing , debugging and maintenance

Dineo Sebothoma( Operations Manager)

Driving operational improvements, maximizing the value of the asset base while
ensuring a tight control on operational costs. Responsible for monitoring and
continually improving standards of performance and quality within the operation.

I will provide with images, logos and the app images.

```html
<!DOCTYPE html>
<html lang="en">
<head>
<meta charset="utf-8">
<title>Povra Company Profile Brochure</title>
<link href="https://fonts.googleapis.com/css2?family=Open+Sans:wght@400;600;700&display=swap" rel="stylesheet">
<style>
  :root {
    --ink: #111111;
    --black: #0b0b0b;
    --paper: #ffffff;
    --paper-grey: #eeeeee;
    --text-dark: #2a2a2a;
    --text-light: #e6e6e6;
    --rule: #e2e2e2;
    --accent: #2f7fc1;
    --stage: #d9d9d9;
  }
  * { box-sizing: border-box; margin: 0; padding: 0; }
  html, body { width: 1200px; height: 921px; overflow: hidden; }
  body {
    background: var(--stage);
    font-family: "Open Sans", Arial, sans-serif;
    color: var(--text-dark);
    position: relative;
  }
  .brochure {
    position: absolute; left: 30px; top: 20px;
    width: 1140px; height: 881px;
    display: flex; background: var(--paper);
    box-shadow: 0 4px 18px rgba(0,0,0,.25);
  }
  .panel { position: relative; width: 380px; height: 100%; overflow: hidden; }
  .hero-photo {
    position: absolute; left: 0; top: 0; width: 760px; height: 310px;
    background: linear-gradient(120deg, #6b625c 0%, #a79b90 35%, #8a8580 60%, #4e4a48 100%);
    z-index: 0;
  }
  .hero-photo::after {
    content: ""; position: absolute; inset: 0;
    background: linear-gradient(90deg, rgba(0,0,0,.35) 0%, rgba(0,0,0,.05) 55%, rgba(0,0,0,.25) 100%);
  }
  .panel-title {
    position: absolute; z-index: 2; color: var(--paper);
    font-weight: 600; font-size: 22px; letter-spacing: .5px;
  }
  .about .panel-title { top: 18px; right: 22px; }
  .about-body {
    position: absolute; top: 310px; left: 0; right: 0; bottom: 110px;
    background: var(--paper-grey); padding: 22px 26px;
  }
  .about-body p { font-size: 12.3px; line-height: 1.55; margin-bottom: 6px; }
  .contact-band {
    position: absolute; left: 0; right: 0; bottom: 0; height: 110px;
    background: var(--black); color: var(--paper);
    display: flex; align-items: center; justify-content: space-between; padding: 0 26px;
  }
  .brand { display: flex; align-items: center; gap: 10px; font-weight: 700; font-size: 30px; color: var(--paper); }
  .brand-dot { width: 22px; height: 22px; border-radius: 50%; background: var(--accent); }
  .contact h3 { font-size: 15px; font-weight: 600; margin-bottom: 8px; text-align: right; }
  .social { display: flex; gap: 8px; justify-content: flex-end; }
  .social span { width: 22px; height: 22px; border-radius: 50%; border: 1.5px solid var(--paper); }

  .how .panel-title { top: 240px; right: 22px; }
  .how .brand-on-photo { position: absolute; z-index: 2; top: 232px; left: 24px; font-size: 26px; }
  .order-label {
    position: absolute; z-index: 2; top: 318px; left: 24px;
    font-size: 18px; font-weight: 700; color: var(--ink);
  }
  .steps { position: absolute; top: 356px; left: 0; right: 0; bottom: 0; list-style: none; }
  .step { display: flex; min-height: 57px; }
  .step-icon {
    width: 52px; flex: none; background: var(--black);
    display: flex; align-items: center; justify-content: center;
  }
  .step-icon svg { width: 22px; height: 22px; fill: none; stroke: var(--paper); stroke-width: 1.8; }
  .step-text {
    flex: 1; padding: 8px 16px; font-size: 12px; line-height: 1.45;
    display: flex; align-items: center; border-bottom: 1px solid var(--rule);
  }

  .team { background: var(--black); color: var(--text-light); padding: 26px 26px; }
  .team-title {
    display: flex; align-items: center; gap: 10px; color: var(--paper);
    font-size: 19px; font-weight: 600; margin-bottom: 18px; white-space: nowrap;
  }
  .team-title::before, .team-title::after { content: ""; flex: 1; height: 1.5px; background: var(--paper); }
  .member { margin-bottom: 14px; }
  .member-head { display: flex; align-items: center; gap: 8px; margin-bottom: 6px; }
  .chevrons {
    background: var(--paper); color: var(--ink); font-size: 9px; font-weight: 700;
    padding: 1px 4px; letter-spacing: -1px;
  }
  .member-name { font-size: 13px; font-weight: 600; color: var(--paper); flex: 1; }
  .member-head svg { width: 14px; height: 14px; fill: var(--paper); }
  .member p { font-size: 11px; line-height: 1.5; margin-bottom: 5px; color: var(--text-light); }
</style>
</head>
<body>
<main class="brochure">
  <div class="hero-photo" role="img" aria-label="Photo of a busy shopping mall interior with shoppers and storefronts"></div>

  <section class="panel about">
    <h2 class="panel-title">About Us</h2>
    <div class="about-body">
      <p>Povra is an on-demand delivery platform where you can order from restaurants, pharmacies, liquor and grocery stores.</p>
      <p>This is the first online digital mall in Africa which will enable you to get back to what you care about which is serving the best liquor in the country.</p>
      <p>Everything is delivered in less than one hour. Customers uses a mobile app to connect with the stores that are within a 6 kilometers radius.</p>
      <p>The nearest driver is notified instantly when there is an order that they need to attend to. We empower communities to shop local with no waiting, and empower businesses through our API to offer delivery.</p>
      <p>We make a real impact on your business when your product is featured in the app, new customers can discover it and loyal customers can have it more often.</p>
      <p>Povra will provide all the relevant stakeholders with insight analytics, ratings and comments regarding all orders fulfilled online via Povra.</p>
    </div>
    <footer class="contact-band">
      <div class="brand"><span class="brand-dot"></span>Povra</div>
      <div class="contact">
        <h3>Contact Us</h3>
        <div class="social"><span></span><span></span><span></span><span></span></div>
      </div>
    </footer>
  </section>

  <section class="panel how">
    <div class="brand brand-on-photo"><span class="brand-dot"></span>Povra</div>
    <h2 class="panel-title">HOW IT WORKS?</h2>
    <div class="order-label">Order</div>
    <ol class="steps">
      <li class="step"><div class="step-icon"><svg viewBox="0 0 24 24"><rect x="7" y="2" width="10" height="20" rx="2"/><line x1="11" y1="18" x2="13" y2="18"/></svg></div><div class="step-text">Customers download the Povra app which is available for Orbit OS and Nimbus OS.</div></li>
      <li class="step"><div class="step-icon"><svg viewBox="0 0 24 24"><circle cx="12" cy="8" r="4"/><path d="M4 21c1-5 15-5 16 0"/></svg></div><div class="step-text">Customers register on the app.</div></li>
      <li class="step"><div class="step-icon"><svg viewBox="0 0 24 24"><path d="M12 22s7-7 7-12a7 7 0 0 0-14 0c0 5 7 12 7 12z"/><circle cx="12" cy="10" r="2.5"/></svg></div><div class="step-text">Set the delivery location to see all the stores around.</div></li>
      <li class="step"><div class="step-icon"><svg viewBox="0 0 24 24"><path d="M3 4h3l2 11h11l2-8H7"/><circle cx="9" cy="19" r="1.5"/><circle cx="17" cy="19" r="1.5"/></svg></div><div class="step-text">Place the order for the item that you want.</div></li>
      <li class="step"><div class="step-icon"><svg viewBox="0 0 24 24"><rect x="2" y="6" width="20" height="12" rx="2"/><circle cx="12" cy="12" r="2.5"/></svg></div><div class="step-text">Pay the cost of the items plus the delivery fee of R40.</div></li>
      <li class="step"><div class="step-icon"><svg viewBox="0 0 24 24"><rect x="2" y="5" width="20" height="14" rx="2"/><line x1="2" y1="10" x2="22" y2="10"/></svg></div><div class="step-text">Payments can be via Credit Card, Debit Cards or Cash on Delivery.</div></li>
      <li class="step"><div class="step-icon"><svg viewBox="0 0 24 24"><path d="M3 17h11V6H3zM14 10h4l3 4v3h-7"/><circle cx="7" cy="18" r="1.8"/><circle cx="17" cy="18" r="1.8"/></svg></div><div class="step-text">Track the progress of the order via the app. Customers can also chat live with the driver or the Povra customer service team.</div></li>
      <li class="step"><div class="step-icon"><svg viewBox="0 0 24 24"><path d="M12 3l2.8 5.8 6.2.9-4.5 4.4 1 6.2L12 17.4 6.5 20.3l1-6.2L3 9.7l6.2-.9z"/></svg></div><div class="step-text">Once Povra has delivered, you are able to rate the service and also provide comments.</div></li>
    </ol>
  </section>

  <section class="panel team">
    <h2 class="team-title">Introducing The Team</h2>

    <article class="member">
      <div class="member-head"><span class="chevrons">&gt;&gt;&gt;&gt;&gt;&gt;&gt;&gt;</span><span class="member-name">Themba Curtis Mabasa (CEO)</span><svg viewBox="0 0 24 24"><circle cx="12" cy="7" r="5"/><path d="M2 23c1-7 19-7 20 0z"/></svg></div>
      <p>He is experienced visioning, costing, innovation and executing projects from inception to launch and is able to provide a structured framework to analyze complex situations into simple strategic imperatives.</p>
      <p>Started Povra as an e-Commerce platform then change the platform to become an on-demand delivery platform which now employers 10 full-time members and 20 independent contractors.</p>
    </article>

    <article class="member">
      <div class="member-head"><span class="chevrons">&gt;&gt;&gt;&gt;&gt;&gt;&gt;&gt;</span><span class="member-name">Richard Molapisi (CTO)</span><svg viewBox="0 0 24 24"><circle cx="12" cy="7" r="5"/><path d="M2 23c1-7 19-7 20 0z"/></svg></div>
      <p>16 years of broad experience in enterprise software architecture, design and development in all stages of software development lifecycle. Experience in scalable and highly available systems. Exceptional understanding of the web infrastructure and ecosystem. Experienced team lead; works well with team members and customers.</p>
      <p>Former Head of Architecture at KELTA leading the Architecture Team and also the Lead Architecture of KELTA Webline Account Portal Project.</p>
    </article>

    <article class="member">
      <div class="member-head"><span class="chevrons">&gt;&gt;&gt;&gt;&gt;&gt;&gt;&gt;</span><span class="member-name">Lesedi Maphanga (Developer)</span><svg viewBox="0 0 24 24"><circle cx="12" cy="7" r="5"/><path d="M2 23c1-7 19-7 20 0z"/></svg></div>
      <p>Accomplished Software Engineer specializing in object-oriented approaches to mobile development. Extensive background in full life-cycle of software development process including requirements gathering, design, coding, testing, debugging and maintenance.</p>
    </article>

    <article class="member">
      <div class="member-head"><span class="member-name">Dineo Sebothoma (Operations Manager)</span></div>
      <p>Driving operational improvements, maximizing the value of the asset base while ensuring a tight control on operational costs. Responsible for monitoring and continually improving standards of performance and quality within the operation.</p>
    </article>
  </section>
</main>
</body>
</html>
```